Corporate Two Sided Business Card

Looking for a Corporate "edgy" Modern look and feel for a business card

We are looking at two options. Dark background with our logo on it, white background with our logo on it - The background is more - Charcoal / Graphite then black

Details will be

Danielle Forsk

Licensee / Director

m. 0428 519 064

e. danielle@quorvela.com.au

quorvela.com.au

Target Market(s)

Professional Business people that refer use business and clients that own Investment Properties

Industry/Entity Type

Business

Contact Information for Business Card

Details will be

Danielle Forsk

Licensee / Director

m. 0428 519 064

quorvela.com.au

Font styles to use
Serif

Colors
000000
ec1f27
eeeeee
ffffff

Requirements
Must have
• Two options - White Background and Dark Background. - Two sided
Nice to have
• A design that is edgy, modern and new to look instead of boring style corporate cards - It should be a full integrated design
Should not have
• Block looking - Cheap.

```html
<!DOCTYPE html>
<html lang="en">
<head>
<meta charset="utf-8">
<title>Quorvela — Business Card</title>
<link rel="stylesheet" href="https://fonts.googleapis.com/css2?family=Arimo:wght@400;700&family=Open+Sans:ital,wght@0,300;1,400&display=swap">
<style>
  :root {
    --stage: #7b7a7b;
    --card-dark: #0d0d0d;
    --card-mid: #2a2a2b;
    --accent: #ec3a45;
    --text-grey: #b9b9b9;
    --text-light: #cfcfcf;
    --icon-ink: #1a1a1a;
  }
  * { box-sizing: border-box; margin: 0; padding: 0; }
  html, body {
    width: 1200px; height: 885px; overflow: hidden;
    background: var(--stage);
  }
  .stage { position: relative; width: 1200px; height: 885px; }
  .card {
    position: absolute; left: 300px; width: 600px; height: 366px;
    border-radius: 3px; overflow: hidden;
    background: linear-gradient(135deg, var(--card-dark) 0%, var(--card-mid) 45%, #1c1c1d 60%, var(--card-dark) 100%);
    box-shadow: 0 10px 26px rgba(0,0,0,.35);
  }
  .card--back { top: 44px; }
  .card--front { top: 475px; }
  .card__texture {
    position: absolute; inset: 0;
    background: radial-gradient(ellipse at 50% 45%, rgba(90,90,92,.35) 0%, rgba(40,40,40,.1) 55%, rgba(0,0,0,0) 80%);
  }

  .brand {
    position: absolute; left: 0; right: 0; top: 150px;
    display: flex; align-items: center; justify-content: center; gap: 12px;
  }
  .brand__mark { width: 22px; height: 22px; background: var(--accent); }
  .brand__name {
    font-family: "Arimo", sans-serif; font-weight: 700;
    font-size: 54px; letter-spacing: 1px; color: var(--text-grey); line-height: 1;
  }

  .person { position: absolute; left: 0; right: 0; top: 112px; text-align: center; }
  .person__name {
    font-family: "Arimo", sans-serif; font-weight: 700; font-size: 40px;
    color: var(--accent); line-height: 1;
  }
  .person__role {
    margin-top: 6px;
    font-family: "Open Sans", sans-serif; font-weight: 300; font-size: 20px;
    color: var(--text-light);
  }

  .contact-rail { position: absolute; left: 34px; top: 222px; width: 532px; height: 34px; }
  .contact-rail__line {
    position: absolute; left: 0; right: 0; top: 14px; height: 7px;
    border-radius: 4px; background: var(--accent);
  }
  .contact-rail__icon {
    position: absolute; top: 0; width: 34px; height: 34px; border-radius: 50%;
    background: var(--accent); border: 3px solid var(--card-dark);
    display: flex; align-items: center; justify-content: center;
  }
  .contact-rail__icon svg { width: 18px; height: 18px; }
  .contact-list {
    position: absolute; left: 34px; top: 270px; width: 532px;
    list-style: none;
  }
  .contact-list li {
    position: absolute; transform: translateX(-50%); white-space: nowrap;
    font-family: "Open Sans", sans-serif; font-style: italic; font-size: 14px;
    color: var(--text-grey);
  }
</style>
</head>
<body>
<main class="stage">

  <section class="card card--back" aria-label="Card back">
    <div class="card__texture" role="img" aria-label="Dark halftone dot texture"></div>
    <div class="brand">
      <span class="brand__mark"></span>
      <span class="brand__name">quorvela</span>
    </div>
  </section>

  <section class="card card--front" aria-label="Card front">
    <div class="card__texture" role="img" aria-label="Dark halftone dot texture"></div>
    <div class="person">
      <h1 class="person__name">Danielle Forsk</h1>
      <p class="person__role">Licensee / Director</p>
    </div>

    <div class="contact-rail">
      <div class="contact-rail__line"></div>
      <span class="contact-rail__icon" style="left:79px">
        <svg viewBox="0 0 24 24" aria-hidden="true"><path fill="var(--icon-ink)" d="M6.6 10.8a15 15 0 0 0 6.6 6.6l2.2-2.2c.3-.3.7-.4 1-.2 1.1.4 2.3.6 3.6.6.6 0 1 .4 1 1V20c0 .6-.4 1-1 1A17 17 0 0 1 3 4c0-.6.4-1 1-1h3.5c.6 0 1 .4 1 1 0 1.3.2 2.5.6 3.6.1.3 0 .7-.2 1z"/></svg>
      </span>
      <span class="contact-rail__icon" style="left:249px">
        <svg viewBox="0 0 24 24" aria-hidden="true"><rect x="3" y="6" width="18" height="12" fill="none" stroke="var(--icon-ink)" stroke-width="2"/><path d="M3 6l9 7 9-7" fill="none" stroke="var(--icon-ink)" stroke-width="2"/></svg>
      </span>
      <span class="contact-rail__icon" style="left:419px">
        <svg viewBox="0 0 24 24" aria-hidden="true"><g fill="none" stroke="var(--icon-ink)" stroke-width="1.8"><circle cx="12" cy="12" r="9"/><ellipse cx="12" cy="12" rx="4" ry="9"/><path d="M3 12h18M5 7h14M5 17h14"/></g></svg>
      </span>
    </div>

    <ul class="contact-list">
      <li style="left:96px">0428 519 064</li>
      <li style="left:266px">danielle@quorvela.com.au</li>
      <li style="left:436px">quorvela.com.au</li>
    </ul>
  </section>

</main>
</body>
</html>
```